Email Advertisement - Designed for airplane buyers to review an airplane.

We need an email ad template to feature an airplane for sale. It should be a clean white type design with no photo shop done inside the photos. It should also be able to be built as a responsive design.

Target Market(s)

Sent to potential aircraft buyers

Industry/Entity Type

Shop

Font styles to use
Sans Serif

Colors
34a6d7
85cae6
ffffff

Requirements
Must have
• Some of the photos may link to a video tour, the website or an email

```html
<!DOCTYPE html>
<html lang="en">
<head>
<meta charset="utf-8">
<title>Skyvale – Aircraft for Sale Email</title>
<link rel="stylesheet" href="https://fonts.googleapis.com/css2?family=Quicksand:wght@400;500;700&display=swap">
<style>
:root{
  --stage:#dcdcdc;
  --blue:#34a6d7;
  --blue-strong:#1a96dc;
  --blue-soft:#85cae6;
  --white:#ffffff;
  --panel-desk:#f3f4f6;
  --ink:#3a3a3a;
  --muted:#6b6b6b;
  --line:#dfe2e6;
  --tick:#b9bcc0;
  --footer:#333333;
  --footer-ink:#e9e9e9;
  --social-a:#3b5a99;
  --social-b:#3aa4dc;
  --social-c:#d9534f;
}
*{box-sizing:border-box;margin:0;padding:0}
html,body{width:1200px;height:2560px;overflow:hidden}
body{background:var(--stage);font-family:"Quicksand",sans-serif;color:var(--ink);position:relative}
a{text-decoration:none;color:inherit}

.preheader{position:absolute;font-size:13px;color:var(--ink);line-height:17px}
.preheader a{color:var(--blue);text-decoration:underline}
.preheader.desk{left:79px;width:568px;top:64px;text-align:center}
.preheader.mob{left:770px;width:270px;top:56px}

.email{position:absolute;top:106px;overflow:hidden}
.email.desk{left:79px;width:568px;height:1734px;background:var(--panel-desk)}
.email.mob{left:734px;width:316px;height:2277px;background:var(--white);box-shadow:0 2px 4px rgba(0,0,0,.15)}
.email > *{position:absolute}

.brand{font-weight:500;color:var(--blue);letter-spacing:1px;text-align:center;line-height:1}
.desk .brand.top{left:134px;top:42px;width:240px;font-size:48px}
.mob .brand.top{left:36px;top:42px;width:240px;font-size:46px}

.unsubscribe{display:flex;align-items:center;justify-content:center;gap:6px;height:41px;border:1px solid var(--line);border-radius:21px;background:var(--white);font-size:12px;font-weight:700;color:var(--blue)}
.desk .unsubscribe{left:421px;top:44px;width:125px}
.mob .unsubscribe{left:96px;top:138px;width:124px}

.photo{display:block}
.hero-photo{background:linear-gradient(180deg,#f4f4f4 0%,#e9e9e9 70%,#b8a48a 88%,#9e8a70 100%)}
.desk .hero-photo{left:23px;top:159px;width:523px;height:230px}
.mob .hero-photo{left:14px;top:210px;width:288px;height:196px}

.hero-band{background:var(--blue-strong);color:var(--white);display:flex;align-items:center;justify-content:center;text-align:center;font-size:22px;font-weight:400;line-height:27px}
.desk .hero-band{left:23px;top:389px;width:523px;height:53px}
.mob .hero-band{left:14px;top:406px;width:288px;height:75px;padding:0 20px}

.plane-icon{width:26px;height:26px}
.desk .plane-icon{left:271px;top:457px}
.mob .plane-icon{left:145px;top:499px}

.listing-title{width:100%;left:0;text-align:center;font-size:21px;font-weight:500;color:var(--blue);letter-spacing:.5px}
.desk .listing-title{top:482px}
.mob .listing-title{top:530px}
.divider{width:36px;height:1px;background:var(--line)}
.desk .divider.a{left:266px;top:531px}
.mob .divider.a{left:140px;top:565px}

.photo-main{background:linear-gradient(180deg,#8fa3b4 0%,#a9b9c2 35%,#6e8a63 65%,#56704b 100%)}
.photo-cockpit{background:linear-gradient(160deg,#2e3a48 0%,#5b6b7c 50%,#202a36 100%)}
.photo-cabin{background:linear-gradient(160deg,#d8c3a3 0%,#a98760 55%,#6f5438 100%)}
.desk .photo-main{left:23px;top:561px;width:373px;height:217px}
.desk .photo-cockpit{left:404px;top:561px;width:143px;height:105px}
.desk .photo-cabin{left:404px;top:673px;width:143px;height:105px}
.mob .photo-main{left:14px;top:596px;width:288px;height:182px}
.mob .photo-cockpit{left:15px;top:785px;width:140px;height:106px}
.mob .photo-cabin{left:162px;top:785px;width:140px;height:106px}

.spec-box{border:1px solid var(--line);background:var(--white)}
.desk .spec-box{left:64px;top:836px;width:441px;height:306px;background:var(--panel-desk)}
.mob .spec-box{left:14px;top:966px;width:286px;height:328px}
.spec-tab{background:var(--blue-strong);color:var(--white);font-size:13px;font-weight:700;display:flex;align-items:center;justify-content:center;height:34px}
.desk .spec-tab{left:206px;top:804px;width:157px}
.mob .spec-tab{left:80px;top:932px;width:159px}

.spec-list{list-style:none}
.desk .spec-list{left:133px;top:864px;width:340px}
.mob .spec-list{left:36px;top:1001px;width:260px}
.spec-row{display:flex;align-items:center;font-size:13px}
.desk .spec-row{height:34px}
.mob .spec-row{height:36.6px}
.spec-row svg{width:15px;height:15px;flex:none}
.spec-label{font-weight:700;color:var(--ink);margin-left:6px}
.spec-value{color:var(--muted);line-height:17px}
.desk .spec-label{width:126px}
.desk .spec-value{width:190px}
.mob .spec-label{width:113px;margin-left:5px}
.mob .spec-value{width:120px}

.btn-outline{display:flex;align-items:center;justify-content:center;border:1px solid #8c8c8c;background:var(--white);font-size:13px;color:var(--ink);height:34px}
.desk .btn-outline{left:225px;top:1082px;width:118px}
.mob .btn-outline{left:101px;top:1237px;width:117px}

.section-title{left:0;width:100%;text-align:center;font-size:21px;font-weight:500;color:var(--blue)}
.desk .section-title{top:1160px}
.mob .section-title{top:1324px}
.desk .divider.b{left:266px;top:1196px}
.mob .divider.b{left:140px;top:1360px}

.collection{display:block;width:160px;text-align:center;font-size:13px;color:var(--ink);line-height:17px}
.collection .thumb{display:block;width:123px;height:123px;border-radius:50%;margin:0 auto 14px}
.thumb.ultralight{background:linear-gradient(160deg,#3f7a5f 0%,#2f5c48 60%,#24493a 100%)}
.thumb.toy{background:linear-gradient(180deg,#cfe0ee 0%,#e8eef3 45%,#6f9a4d 75%,#3e6b2c 100%)}
.thumb.horizon{background:linear-gradient(180deg,#9eb7d2 0%,#c4d0dc 50%,#7d8ea3 75%,#55657a 100%)}
.desk .collection.c1{left:25px;top:1225px}
.desk .collection.c2{left:205px;top:1225px}
.desk .collection.c3{left:384px;top:1225px}
.mob .collection{left:78px}
.mob .collection.c1{top:1386px}
.mob .collection.c2{top:1578px}
.mob .collection.c3{top:1759px}

.btn-solid{display:flex;align-items:center;justify-content:center;background:var(--blue-strong);color:var(--white);font-size:14px;height:36px}
.desk .btn-solid{left:225px;top:1429px;width:119px}
.mob .btn-solid{left:96px;top:1953px;width:119px}

.footer{left:0;width:100%;background:var(--footer);color:var(--footer-ink);text-align:center;font-size:13px}
.desk .footer{top:1529px;height:205px}
.mob .footer{top:2028px;height:249px}
.footer > *{position:absolute;left:0;width:100%}
.brand.foot{font-size:30px;opacity:.9}
.desk .brand.foot{top:42px}
.mob .brand.foot{top:41px}
.social{display:flex;justify-content:center;list-style:none}
.social li{width:28px;height:28px}
.social .s1{background:var(--social-a)}
.social .s2{background:var(--social-b)}
.social .s3{background:var(--social-c)}
.desk .social{top:99px;gap:14px}
.mob .social{top:98px;gap:5px}
.contact{line-height:21px}
.desk .contact{top:140px}
.mob .contact{top:145px;padding:0 40px}
</style>
</head>
<body>

<p class="preheader desk">For anything about this mail you can contract us by <a href="#">click this link.</a></p>
<p class="preheader mob">For anything about this mail you can<br>contract us by <a href="#">click this link.</a></p>

<article class="email desk">
  <div class="brand top">Skyvale</div>
  <a class="unsubscribe" href="#">
    <svg width="14" height="14" viewBox="0 0 16 16" aria-hidden="true"><path d="M13 8a5 5 0 0 1-9 3M3 8a5 5 0 0 1 9-3" fill="none" stroke="currentColor" stroke-width="2"/><path d="M12 1v4H8M4 15v-4h4" fill="none" stroke="currentColor" stroke-width="2"/></svg>Unsubscribe</a>
  <a class="photo hero-photo" href="#" role="img" aria-label="Photo of a model airliner on a stand, light studio backdrop"></a>
  <div class="hero-band">Wellcome to Airoplane Buying</div>
  <svg class="plane-icon" viewBox="0 0 24 24" aria-hidden="true"><path d="M2 12h20M14 12l-5-7h-2l3 7M14 12l-5 7h-2l3-7M4 12l-2-3M4 12l-2 3" fill="none" stroke="#c4c7cb" stroke-width="1.4"/></svg>
  <h1 class="listing-title">1975 VOLKOV VK 50</h1>
  <span class="divider a"></span>
  <a class="photo photo-main" href="#" role="img" aria-label="Photo of the business jet in flight over farmland"></a>
  <a class="photo photo-cockpit" href="#" role="img" aria-label="Photo of the cockpit instrument panel"></a>
  <a class="photo photo-cabin" href="#" role="img" aria-label="Photo of the leather cabin interior"></a>
  <div class="spec-box"></div>
  <div class="spec-tab">Full Specification</div>
  <ul class="spec-list">
    <li class="spec-row"><svg viewBox="0 0 16 16" aria-hidden="true"><circle cx="8" cy="8" r="8" fill="var(--tick)"/><path d="M4.5 8.3l2.3 2.2 4.7-4.8" fill="none" stroke="#fff" stroke-width="1.8"/></svg><span class="spec-label">Sale Status:</span><span class="spec-value">For Sale</span></li>
    <li class="spec-row"><svg viewBox="0 0 16 16" aria-hidden="true"><circle cx="8" cy="8" r="8" fill="var(--tick)"/><path d="M4.5 8.3l2.3 2.2 4.7-4.8" fill="none" stroke="#fff" stroke-width="1.8"/></svg><span class="spec-label">Year:</span><span class="spec-value">2017</span></li>
    <li class="spec-row"><svg viewBox="0 0 16 16" aria-hidden="true"><circle cx="8" cy="8" r="8" fill="var(--tick)"/><path d="M4.5 8.3l2.3 2.2 4.7-4.8" fill="none" stroke="#fff" stroke-width="1.8"/></svg><span class="spec-label">Make/Model:</span><span class="spec-value">HARROW AERO KESTREL</span></li>
    <li class="spec-row"><svg viewBox="0 0 16 16" aria-hidden="true"><circle cx="8" cy="8" r="8" fill="var(--tick)"/><path d="M4.5 8.3l2.3 2.2 4.7-4.8" fill="none" stroke="#fff" stroke-width="1.8"/></svg><span class="spec-label">Registration #:</span><span class="spec-value">N718SV</span></li>
    <li class="spec-row"><svg viewBox="0 0 16 16" aria-hidden="true"><circle cx="8" cy="8" r="8" fill="var(--tick)"/><path d="M4.5 8.3l2.3 2.2 4.7-4.8" fill="none" stroke="#fff" stroke-width="1.8"/></svg><span class="spec-label">Serial #:</span><span class="spec-value">240-0583</span></li>
    <li class="spec-row"><svg viewBox="0 0 16 16" aria-hidden="true"><circle cx="8" cy="8" r="8" fill="var(--tick)"/><path d="M4.5 8.3l2.3 2.2 4.7-4.8" fill="none" stroke="#fff" stroke-width="1.8"/></svg><span class="spec-label">Location</span><span class="spec-value">Ashford, IN USA</span></li>
  </ul>
  <a class="btn-outline" href="#">Enquire Now</a>
  <h2 class="section-title">New Collections</h2>
  <span class="divider b"></span>
  <a class="collection c1" href="#"><span class="thumb ultralight" role="img" aria-label="Photo of an ultralight aircraft over green water"></span>Ultralight Aircraft</a>
  <a class="collection c2" href="#"><span class="thumb toy" role="img" aria-label="Photo of a toy model plane over a meadow"></span>Tern Toys T310</a>
  <a class="collection c3" href="#"><span class="thumb horizon" role="img" aria-label="Photo of a single-engine plane in a blue sky"></span>2013 CORVAN<br>HORIZON</a>
  <a class="btn-solid" href="#">See More</a>
  <footer class="footer">
    <div class="brand foot">Skyvale</div>
    <ul class="social" aria-label="Social links"><li class="s1"></li><li class="s2"></li><li class="s3"></li></ul>
    <p class="contact">Phone: + 971 4 000 12 34 | Mobile: + 971 50 000 56 78<br>E-mail: hello@skyvale.example | Web: www.skyvale.example</p>
  </footer>
</article>

<article class="email mob">
  <div class="brand top">Skyvale</div>
  <a class="unsubscribe" href="#">
    <svg width="14" height="14" viewBox="0 0 16 16" aria-hidden="true"><path d="M13 8a5 5 0 0 1-9 3M3 8a5 5 0 0 1 9-3" fill="none" stroke="currentColor" stroke-width="2"/><path d="M12 1v4H8M4 15v-4h4" fill="none" stroke="currentColor" stroke-width="2"/></svg>Unsubscribe</a>
  <a class="photo hero-photo" href="#" role="img" aria-label="Photo of a model airliner on a stand, light studio backdrop"></a>
  <div class="hero-band">Wellcome to Airoplane Buying</div>
  <svg class="plane-icon" viewBox="0 0 24 24" aria-hidden="true"><path d="M2 12h20M14 12l-5-7h-2l3 7M14 12l-5 7h-2l3-7M4 12l-2-3M4 12l-2 3" fill="none" stroke="#c4c7cb" stroke-width="1.4"/></svg>
  <h1 class="listing-title">1975 VOLKOV VK 50</h1>
  <span class="divider a"></span>
  <a class="photo photo-main" href="#" role="img" aria-label="Photo of the business jet in flight over farmland"></a>
  <a class="photo photo-cockpit" href="#" role="img" aria-label="Photo of the cockpit instrument panel"></a>
  <a class="photo photo-cabin" href="#" role="img" aria-label="Photo of the leather cabin interior"></a>
  <div class="spec-box"></div>
  <div class="spec-tab">Full Specification</div>
  <ul class="spec-list">
    <li class="spec-row"><svg viewBox="0 0 16 16" aria-hidden="true"><circle cx="8" cy="8" r="8" fill="var(--tick)"/><path d="M4.5 8.3l2.3 2.2 4.7-4.8" fill="none" stroke="#fff" stroke-width="1.8"/></svg><span class="spec-label">Sale Status:</span><span class="spec-value">For Sale</span></li>
    <li class="spec-row"><svg viewBox="0 0 16 16" aria-hidden="true"><circle cx="8" cy="8" r="8" fill="var(--tick)"/><path d="M4.5 8.3l2.3 2.2 4.7-4.8" fill="none" stroke="#fff" stroke-width="1.8"/></svg><span class="spec-label">Year:</span><span class="spec-value">2017</span></li>
    <li class="spec-row"><svg viewBox="0 0 16 16" aria-hidden="true"><circle cx="8" cy="8" r="8" fill="var(--tick)"/><path d="M4.5 8.3l2.3 2.2 4.7-4.8" fill="none" stroke="#fff" stroke-width="1.8"/></svg><span class="spec-label">Make/Model:</span><span class="spec-value">HARROW AERO KESTREL</span></li>
    <li class="spec-row"><svg viewBox="0 0 16 16" aria-hidden="true"><circle cx="8" cy="8" r="8" fill="var(--tick)"/><path d="M4.5 8.3l2.3 2.2 4.7-4.8" fill="none" stroke="#fff" stroke-width="1.8"/></svg><span class="spec-label">Registration #:</span><span class="spec-value">N718SV</span></li>
    <li class="spec-row"><svg viewBox="0 0 16 16" aria-hidden="true"><circle cx="8" cy="8" r="8" fill="var(--tick)"/><path d="M4.5 8.3l2.3 2.2 4.7-4.8" fill="none" stroke="#fff" stroke-width="1.8"/></svg><span class="spec-label">Serial #:</span><span class="spec-value">240-0583</span></li>
    <li class="spec-row"><svg viewBox="0 0 16 16" aria-hidden="true"><circle cx="8" cy="8" r="8" fill="var(--tick)"/><path d="M4.5 8.3l2.3 2.2 4.7-4.8" fill="none" stroke="#fff" stroke-width="1.8"/></svg><span class="spec-label">Location</span><span class="spec-value">Ashford, IN USA</span></li>
  </ul>
  <a class="btn-outline" href="#">Enquire Now</a>
  <h2 class="section-title">New Collections</h2>
  <span class="divider b"></span>
  <a class="collection c1" href="#"><span class="thumb ultralight" role="img" aria-label="Photo of an ultralight aircraft over green water"></span>Ultralight Aircraft</a>
  <a class="collection c2" href="#"><span class="thumb toy" role="img" aria-label="Photo of a toy model plane over a meadow"></span>Tern Toys T310</a>
  <a class="collection c3" href="#"><span class="thumb horizon" role="img" aria-label="Photo of a single-engine plane in a blue sky"></span>2013 CORVAN<br>HORIZON</a>
  <a class="btn-solid" href="#">See More</a>
  <footer class="footer">
    <div class="brand foot">Skyvale</div>
    <ul class="social" aria-label="Social links"><li class="s1"></li><li class="s2"></li><li class="s3"></li></ul>
    <p class="contact">Phone: + 971 4 000 12 34 |<br>Mobile: + 971 50 000 56 78<br>E-mail: hello@skyvale.example |<br>Web: www.skyvale.example</p>
  </footer>
</article>

</body>
</html>
```